Carpentry company Needs a business card design

We need a design for a Carpentry / building company, business card. Please think of designs out of the ordinary and try to make it eye catching. Our existing logo will need to be incorporated in the design. However feel free to change the colours of the logo to suit your design. I would like to see some designs with green /black and orange incorporated into it.These are not the only colours accepted and all designs that appeal will be accepted.

Please contact me should you have any questions
Thanks Martin

Target Market(s)

General Public seeking carpentry work

Industry/Entity Type

Business

Contact Information for Business Card

- Current company logo ( colours can be changed)
-Phone number ,
- info@brelvanbuild.com.au
- brelvanbuild.com.au
-the facebook symbol

Font styles to use
Other font styles liked:
• You choose

Requirements
Must have
• Services we provide
• - Renovations
• -Deckings & Pergolas
• -Kitchens
• - Bathrooms
• - Intricate details
Nice to have
• an awesome design
Should not have
• Tools on the business card

```html
<!DOCTYPE html>
<html lang="en">
<head>
<meta charset="utf-8">
<title>Brelvan Build — Business Card</title>
<link href="https://fonts.googleapis.com/css2?family=Arimo:wght@400;700&display=swap" rel="stylesheet">
<style>
  :root {
    --stage: #d8d6d3;
    --paper: #ffffff;
    --espresso: #23130f;
    --copper: #d5822e;
    --rust: #87512a;
    --ink: #1c1412;
    --rule: #bdbdbd;
    --title-text: #ece4e0;
    --olive: #4c4426;   --olive-text: #dcd9b0;
    --walnut: #7a4825;  --walnut-text: #f3cfa4;
    --slate: #333e48;   --slate-text: #b8cde0;
    --oak: #6e5a34;     --oak-text: #f4e6b0;
    --wine: #6c1a28;    --wine-text: #f2a8c0;
  }
  * { margin: 0; padding: 0; box-sizing: border-box; }
  html, body { width: 1200px; height: 1200px; overflow: hidden; }
  body {
    background: var(--stage);
    font-family: "Arimo", Arial, sans-serif;
    position: relative;
  }
  .card {
    position: absolute;
    left: 169px;
    width: 882px;
    height: 476px;
    overflow: hidden;
    box-shadow: 0 4px 14px rgba(0,0,0,.25);
  }
  /* Front */
  .card--front { top: 73px; background: var(--espresso); }
  .front__face {
    position: absolute; left: 0; top: 0;
    width: 100%; height: 395px;
    background: var(--paper);
  }
  .brand {
    position: absolute; left: 68px; top: 136px;
    width: 330px;
    display: flex; align-items: center; gap: 14px;
  }
  .brand__square { width: 22px; height: 22px; background: var(--copper); flex: none; }
  .brand__name {
    font-weight: 700; font-size: 52px; letter-spacing: 1px;
    color: var(--ink); line-height: 56px;
  }
  .divider {
    position: absolute; left: 424px; top: 84px;
    width: 1px; height: 254px; background: var(--copper);
  }
  .contact {
    position: absolute; left: 456px; top: 124px; width: 356px;
    border-top: 1px solid var(--rule);
    border-bottom: 1px solid var(--rule);
    padding: 25px 0 21px;
    list-style: none;
  }
  .contact__item {
    display: flex; align-items: center; gap: 10px;
    font-size: 25px; font-weight: 400; color: var(--ink);
    line-height: 34px; white-space: nowrap;
  }
  .contact__item--phone { font-weight: 700; }
  .contact__icon { width: 24px; height: 24px; flex: none; }
  /* Back */
  .card--back { top: 607px; background: var(--espresso); }
  .services__title {
    position: absolute; left: 0; top: 36px;
    width: 770px; height: 84px;
    background: var(--rust);
    color: var(--title-text);
    font-weight: 700; font-size: 59px;
    padding-left: 149px; line-height: 84px;
    white-space: nowrap;
  }
  .rule {
    position: absolute; height: 2px; background: var(--rust);
  }
  .rule--top { left: 141px; width: 617px; top: 133px; }
  .rule--bottom { left: 138px; width: 617px; top: 439px; }
  .services__list { list-style: none; position: absolute; left: 0; top: 164px; }
  .service {
    height: 49px; margin-bottom: 1px;
    padding-left: 142px;
    font-weight: 700; font-size: 40px; line-height: 49px;
    white-space: nowrap;
  }
  .service--renovations { width: 452px; background: var(--olive); color: var(--olive-text); }
  .service--decking { width: 560px; background: var(--walnut); color: var(--walnut-text); }
  .service--kitchens { width: 356px; background: var(--slate); color: var(--slate-text); }
  .service--bathrooms { width: 373px; background: var(--oak); color: var(--oak-text); }
  .service--details { width: 452px; background: var(--wine); color: var(--wine-text); }
</style>
</head>
<body>
  <section class="card card--front" aria-label="Business card front">
    <div class="front__face">
      <div class="brand">
        <span class="brand__square"></span>
        <span class="brand__name">BRELVAN<br>BUILD</span>
      </div>
      <div class="divider"></div>
      <ul class="contact">
        <li class="contact__item contact__item--phone">
          <svg class="contact__icon" viewBox="0 0 24 24" aria-hidden="true">
            <path d="M2 9c0-3 4-5 10-5s10 2 10 5v2h-5V8H7v3H2z" fill="#d5822e"/>
            <path d="M6 12h12l2 8H4z" fill="#d5822e"/>
            <circle cx="12" cy="16" r="2.2" fill="#fff"/>
          </svg>
          +61 400 555 018
        </li>
        <li class="contact__item">
          <svg class="contact__icon" viewBox="0 0 24 24" aria-hidden="true">
            <rect x="2" y="2" width="20" height="20" rx="3" fill="#d5822e"/>
          </svg>
          facebook.com/brelvanbuild
        </li>
        <li class="contact__item">
          <svg class="contact__icon" viewBox="0 0 24 24" aria-hidden="true">
            <circle cx="12" cy="12" r="10" fill="none" stroke="#d5822e" stroke-width="1.5"/>
            <path d="M2 12h20" stroke="#d5822e" stroke-width="1.2"/>
          </svg>
          brelvanbuild.com.au
        </li>
      </ul>
    </div>
  </section>

  <section class="card card--back" aria-label="Business card back">
    <h2 class="services__title">Services we provide</h2>
    <div class="rule rule--top"></div>
    <ul class="services__list">
      <li class="service service--renovations">Renovations</li>
      <li class="service service--decking">Deckings &amp; Pergolas</li>
      <li class="service service--kitchens">Kitchens</li>
      <li class="service service--bathrooms">Bathrooms</li>
      <li class="service service--details">Intricate details</li>
    </ul>
    <div class="rule rule--bottom"></div>
  </section>
</body>
</html>
```